Business Card Design Project

Recently had a new logo made up for my company and new business cards done as well. I have attached the logos for your viewing. Additional projects may be needed. Good luck!

Business

```html
<!DOCTYPE html>
<html lang="en">
<head>
<meta charset="utf-8">
<title>Harwell Financial Group – Business Card</title>
<link rel="stylesheet" href="https://fonts.googleapis.com/css2?family=Open+Sans:wght@400;600&display=swap">
<style>
  :root {
    --backdrop: #3b3b3d;
    --card: #1f1f27;
    --card-sheen: #2a2a33;
    --gold: #c9b27a;
    --text: #ffffff;
    --text-soft: #e6e6ea;
  }
  * { box-sizing: border-box; margin: 0; padding: 0; }
  html, body { width: 1200px; height: 900px; overflow: hidden; }
  body {
    background: var(--backdrop);
    font-family: "Open Sans", Arial, sans-serif;
    position: relative;
  }
  .card {
    position: absolute;
    top: 307px;
    width: 516px;
    height: 285px;
    background: linear-gradient(115deg, var(--card) 0%, var(--card) 62%, var(--card-sheen) 62.2%, var(--card) 100%);
    box-shadow: 0 6px 14px rgba(0,0,0,.55);
  }
  .card--front { left: 73px; }
  .card--back { left: 615px; }

  /* Front */
  .front-brand {
    position: absolute;
    left: 0; right: 0; top: 42px;
    display: flex; flex-direction: column; align-items: center;
  }
  .brand-square {
    width: 126px; height: 134px;
    border: 8px solid var(--gold);
  }
  .front-brand .brand-name {
    margin-top: 16px;
    color: var(--gold);
    font-weight: 600;
    font-size: 22px;
    letter-spacing: 1.5px;
    text-transform: uppercase;
    text-align: center;
    line-height: 1.2;
  }

  /* Back */
  .back-brand {
    position: absolute;
    left: 34px; top: 27px;
    display: flex; align-items: center; gap: 8px;
  }
  .back-brand .brand-mark {
    width: 48px; height: 50px;
    border: 3px solid var(--gold);
  }
  .back-brand .brand-name {
    color: var(--gold);
    font-weight: 600;
    font-size: 22px;
    letter-spacing: 1px;
    text-transform: uppercase;
  }
  .holder {
    position: absolute;
    left: 34px; top: 142px;
  }
  .holder-name {
    color: var(--gold);
    font-size: 19px;
    font-weight: 400;
  }
  .holder-title {
    color: var(--text);
    font-size: 11.5px;
    margin-top: 4px;
  }
  .divider {
    position: absolute;
    left: 0; right: 0; top: 196px;
    height: 2px;
    background: var(--gold);
  }
  .contact {
    position: absolute;
    top: 208px;
    list-style: none;
    color: var(--text-soft);
    font-size: 12px;
    line-height: 17.5px;
  }
  .contact--direct { left: 34px; }
  .contact--office { left: 292px; }
  .contact .label { color: var(--gold); }
</style>
</head>
<body>
  <section class="card card--front" aria-label="Card front">
    <div class="front-brand">
      <div class="brand-square" aria-hidden="true"></div>
      <p class="brand-name">Harwell<br>Financial Group</p>
    </div>
  </section>

  <section class="card card--back" aria-label="Card back">
    <div class="back-brand">
      <div class="brand-mark" aria-hidden="true"></div>
      <p class="brand-name">Harwell Financial Group</p>
    </div>

    <div class="holder">
      <p class="holder-name">Daniel R. Harwell</p>
      <p class="holder-title">Estate Planning and Insurance Specialist</p>
    </div>

    <div class="divider"></div>

    <ul class="contact contact--direct">
      <li><span class="label">P:</span> 555-210-4837</li>
      <li><span class="label">F:</span> 555-210-4839</li>
      <li><span class="label">E:</span> dharwell@harwellfinancial.com</li>
    </ul>
    <ul class="contact contact--office">
      <li>4120 Meadow Ridge Road, Suite 310E</li>
      <li>Brookdale, New York 11604</li>
      <li>www.harwellfinancial.com</li>
    </ul>
  </section>
</body>
</html>
```